Investment company needing business card

We are wanting a business card which looks sharp and easy on the eye. We are thinking of having a business card with the logo embossed on it, to really make it stand out. We will only have a small amount of information of the business card, person's name, position, email address and phone number

Contact Information for Business Card

Danica Pruett
Executive Assistant
+64 21 547 3162
danicap@harwellcapital.co.nz

Requirements
Must have
• Embossed logo
Should not have
• Not to be busy

```html
<!DOCTYPE html>
<html lang="en">
<head>
<meta charset="UTF-8">
<title>Harwell Capital — Business Card</title>
<link href="https://fonts.googleapis.com/css2?family=Lato:wght@400;700;900&display=swap" rel="stylesheet">
<style>
  :root {
    --brand-green: #25b574;
    --brand-grey: #5f6061;
    --text-grey: #4a4a4a;
    --card-white: #ffffff;
    --backdrop: #e9eaec;
  }
  * { box-sizing: border-box; margin: 0; padding: 0; }
  html, body {
    width: 1200px; height: 800px; overflow: hidden;
    background: var(--backdrop);
    font-family: 'Lato', sans-serif;
  }
  .stage {
    position: relative; width: 1200px; height: 800px;
  }
  .card {
    position: absolute; top: 250px;
    width: 520px; height: 300px;
    overflow: hidden;
    box-shadow: 0 10px 28px rgba(0,0,0,0.18);
  }
  .card--front { left: 53px; background: var(--brand-green); }
  .card--back { left: 627px; background: var(--card-white); }

  .wordmark {
    position: absolute;
    display: flex; align-items: center; gap: 14px;
  }
  .wordmark__square { width: 46px; height: 46px; border-radius: 6px; }
  .wordmark__name {
    font-weight: 900; font-size: 30px; letter-spacing: 2px;
    text-transform: uppercase; line-height: 1;
  }
  .card--front .wordmark { left: 50%; top: 50%; transform: translate(-50%, -50%); }
  .card--front .wordmark__square { background: var(--card-white); }
  .card--front .wordmark__name { color: var(--card-white); }

  .card__corner { position: absolute; inset: 0; }
  .card--back .wordmark { left: 40px; top: 110px; }
  .card--back .wordmark__square { background: var(--brand-grey); }
  .card--back .wordmark__name { color: var(--brand-green); font-size: 27px; }

  .contact { position: absolute; left: 40px; bottom: 30px; }
  .contact__name { color: var(--brand-green); font-weight: 700; font-size: 17px; }
  .contact__role { color: var(--text-grey); font-size: 13px; margin-bottom: 12px; }
  .contact__line {
    display: flex; align-items: center; gap: 8px;
    color: var(--text-grey); font-size: 12.5px; line-height: 1.6;
  }
  .contact__icon { width: 12px; height: 12px; flex: none; }
</style>
</head>
<body>
<main class="stage">
  <section class="card card--front" aria-label="Card front">
    <div class="wordmark">
      <span class="wordmark__square"></span>
      <span class="wordmark__name">Harwell Capital</span>
    </div>
  </section>

  <section class="card card--back" aria-label="Card back">
    <svg class="card__corner" width="520" height="300" viewBox="0 0 520 300" aria-hidden="true">
      <rect width="520" height="300" fill="var(--brand-green)"/>
      <circle cx="-12" cy="488" r="606" fill="var(--brand-grey)"/>
      <circle cx="0" cy="500" r="590" fill="var(--card-white)"/>
    </svg>
    <div class="wordmark">
      <span class="wordmark__square"></span>
      <span class="wordmark__name">Harwell Capital</span>
    </div>
    <div class="contact">
      <p class="contact__name">Danica Pruett</p>
      <p class="contact__role">Executive Assistant</p>
      <p class="contact__line">
        <svg class="contact__icon" viewBox="0 0 12 12" aria-hidden="true">
          <rect x="2.5" y="0.5" width="7" height="11" rx="1.5" fill="none" stroke="var(--brand-green)" stroke-width="1.2"/>
          <line x1="5" y1="9.5" x2="7" y2="9.5" stroke="var(--brand-green)" stroke-width="1.2"/>
        </svg>
        +64 21 547 3162
      </p>
      <p class="contact__line">
        <svg class="contact__icon" viewBox="0 0 12 12" aria-hidden="true">
          <rect x="0.5" y="2" width="11" height="8" fill="var(--brand-green)"/>
          <polyline points="0.5,2 6,6.5 11.5,2" fill="none" stroke="var(--card-white)" stroke-width="1"/>
        </svg>
        danicap@harwellcapital.co.nz
      </p>
    </div>
  </section>
</main>
</body>
</html>
```